Florida-based Coastal Landscaping Comapny Needs Postcard Designs

We are a newly established Florida-based, coastal landscaping company that is looking for some really innovative postcards that we can use to get our name our to affluent consumers that live on the coast of Florida (think on the beach) and small to medium sized businesses in the same area. We will be sending out 100s of thousands of these, so need a great design

Target Market(s)

Affluent consumers and small to medium sized businesses

Industry/Entity Type

Landscaping

Font styles to use
Sans Serif

Colors

Designer to choose colors to be used in the design.

Requirements
Must have
• Florida - looking, island looking / paradise, but incorporate landscaping themes
• Need to say something about "Enjoy your yard this summer" or something relating to summer, landscapes and florida
• and would like to make two offers $50.00 off with signing up for one of our routine maintenance programs, or 1 free landscape inspection
Should not have
• Regular generic lawn company designs. We are a top tier landscape design / build plus maintenance firm, so not your mom and pop lawn mowing company

```html
<!DOCTYPE html>
<html lang="en">
<head>
<meta charset="utf-8">
<title>Shore Gardens – Summer Postcards</title>
<link href="https://fonts.googleapis.com/css2?family=Oswald:wght@300;400;500&family=Open+Sans:wght@400;600&family=Courgette&display=swap" rel="stylesheet">
<style>
  :root{
    --blue:#1ba9d6;
    --blue-deep:#0f8fbb;
    --ink:#222629;
    --charcoal:#2d3134;
    --charcoal-light:#4a4f53;
    --white:#ffffff;
    --paper:#f1f2f3;
    --stage:#e7e7e5;
    --text-dark:#3a3d40;
  }
  *{box-sizing:border-box;margin:0;padding:0}
  html,body{width:858px;height:1200px;overflow:hidden}
  body{background:var(--stage);position:relative;font-family:"Open Sans",Arial,sans-serif}

  .postcard{position:absolute;left:101px;width:656px;height:470px;background:var(--white);overflow:hidden;box-shadow:0 6px 14px rgba(0,0,0,.28)}
  .postcard--front{top:108px}
  .postcard--back{top:645px}

  .photo{position:absolute}
  .brand-name{font-family:"Oswald",sans-serif;font-weight:400;letter-spacing:2px;text-transform:uppercase}
  .tagline{font-family:"Courgette",cursive;position:absolute}
  .condensed{font-family:"Oswald",sans-serif}

  /* front */
  .front__hero{left:0;top:0;width:390px;height:216px;background:linear-gradient(180deg,#4d8fd0 0%,#9cc6e6 35%,#f1f1ec 55%,#6b8a58 85%,#3e6a3a 100%)}
  .front__brand{position:absolute;left:390px;top:0;width:266px;height:154px;background:var(--white)}
  .front__brand .brand-name{position:absolute;left:0;right:0;top:44px;text-align:center;font-size:28px;color:var(--text-dark)}
  .front__brand .tagline{left:0;right:0;top:108px;text-align:center;font-size:17px;color:var(--ink)}
  .front__services{position:absolute;left:372px;top:154px;width:284px;height:94px;background:var(--blue);border-top:2px solid var(--white);border-bottom:2px solid var(--white)}
  .services-list{list-style:none;position:absolute;left:32px;top:14px;display:grid;grid-template-columns:118px 118px;row-gap:7px}
  .services-list li{font-family:"Oswald",sans-serif;font-weight:300;font-size:12.5px;color:var(--white);display:flex;align-items:center;gap:6px;line-height:16px}
  .tick{width:10px;height:10px;flex:none}
  .guarantee-seal{position:absolute;left:301px;top:167px;width:76px;height:76px;border-radius:50%;background:var(--blue);border:4px solid var(--white);box-shadow:0 0 0 2px var(--blue)}
  .front__offer{position:absolute;left:372px;top:248px;width:284px;height:222px;background:radial-gradient(circle at 60% 40%,var(--charcoal-light),var(--ink) 75%);text-align:center;color:var(--white)}
  .offer-amount{font-family:"Oswald",sans-serif;font-weight:500;font-size:27px;color:var(--blue);margin-top:34px;line-height:32px}
  .offer-amount small{font-size:19px}
  .offer-terms{font-size:12.5px;line-height:24px;margin-top:4px}
  .offer-alt{font-family:"Oswald",sans-serif;font-size:16px;letter-spacing:1.5px;color:var(--blue);margin-top:1px}
  .offer-rule{width:200px;height:1px;background:rgba(255,255,255,.35);margin:22px auto 0}
  .offer-web{font-family:"Oswald",sans-serif;font-size:14px;margin-top:16px;letter-spacing:.3px}
  .tile{position:absolute}
  .tile--dark{background:linear-gradient(180deg,#3a3e41,var(--ink));color:var(--white);text-align:center;font-family:"Oswald",sans-serif}
  .tile--estimates{left:0;top:216px;width:126px;height:96px}
  .tile--estimates strong{display:block;font-weight:400;font-size:40px;color:var(--blue);line-height:46px;margin-top:10px}
  .tile--estimates span{display:block;font-size:18px;color:var(--blue);margin-top:2px}
  .tile--licensed{left:129px;top:316px;width:124px;height:98px;padding-top:12px;color:var(--blue);font-weight:300}
  .tile--licensed span{display:block;font-size:17px;line-height:20px}
  .tile--licensed strong{display:block;font-weight:400;font-size:24px;line-height:26px}
  .photo--garden-bed{left:129px;top:216px;width:124px;height:96px;background:linear-gradient(160deg,#5f7b47,#b3505a 50%,#4c7a38)}
  .photo--paver-path{left:257px;top:216px;width:133px;height:198px;background:linear-gradient(170deg,#5a7d44,#9a6a55 50%,#c9887b 75%,#6f8a4b)}
  .photo--pool-deck{left:0;top:316px;width:126px;height:98px;background:linear-gradient(160deg,#466b3c,#8fb8c0 45%,#d7dcd8 70%,#4c7a3a)}
  .front__call{position:absolute;left:0;top:414px;width:372px;height:56px;background:var(--paper);display:flex;align-items:center;padding-left:40px;gap:12px}
  .call-label{font-family:"Oswald",sans-serif;font-weight:500;font-size:28px;color:var(--blue)}
  .call-phone{font-family:"Oswald",sans-serif;font-weight:500;font-size:17px;color:var(--blue);display:flex;align-items:center;gap:6px}
  .phone-icon{width:17px;height:17px}
  .swoosh{position:absolute;left:0;top:0;pointer-events:none}

  /* back */
  .back__hero{left:0;top:0;width:656px;height:230px;background:linear-gradient(180deg,#27351f 0%,#4b5a34 30%,#2f7d78 60%,#6a7d48 85%,#caa36a 100%)}
  .back__panel-shape{position:absolute;left:0;top:0}
  .back__content{position:absolute;left:0;top:0;width:400px;height:470px;color:var(--white)}
  .back__content .brand-name{position:absolute;left:0;width:314px;top:172px;text-align:center;font-size:24px;color:var(--white)}
  .back__content .tagline{left:0;width:314px;top:226px;text-align:center;font-size:20px;color:var(--white)}
  .features-list{list-style:none;position:absolute;left:36px;top:272px}
  .features-list li{font-size:14px;line-height:22.6px;display:flex;align-items:center;gap:12px}
  .back__rule{position:absolute;left:20px;top:380px;width:320px;height:1px;background:linear-gradient(90deg,var(--blue),rgba(27,169,214,.1))}
  .back__call{position:absolute;left:20px;top:389px;display:flex;align-items:center;gap:10px}
  .back__call .call-label{font-size:27px}
  .back__web{position:absolute;left:59px;top:430px;font-family:"Oswald",sans-serif;font-size:13.5px;letter-spacing:.3px}
  .offer-bubble{position:absolute;border-radius:50%;background:var(--blue);border:3px solid var(--white);box-shadow:0 3px 8px rgba(0,0,0,.3);color:var(--white);font-family:"Oswald",sans-serif;display:flex;flex-direction:column;align-items:center;justify-content:center;text-align:center}
  .offer-bubble--discount{left:404px;top:129px;width:92px;height:92px;font-size:17px}
  .offer-bubble--discount small{font-size:12px}
  .offer-bubble--inspection{left:505px;top:93px;width:120px;height:120px;font-size:14px;line-height:18px;font-weight:300}
</style>
</head>
<body>

<article class="postcard postcard--front">
  <div class="photo front__hero" role="img" aria-label="Photo of a white coastal villa with palm trees and a pool"></div>

  <div class="front__brand">
    <div class="brand-name">Shore Gardens</div>
    <p class="tagline">Enjoy your yard this summer</p>
  </div>

  <div class="front__services">
    <ul class="services-list">
      <li><svg class="tick" viewBox="0 0 10 10"><circle cx="5" cy="5" r="5" fill="#fff"/><path d="M2.6 5.2l1.6 1.6 3.2-3.4" stroke="#1ba9d6" stroke-width="1.4" fill="none"/></svg>Landscaping</li>
      <li><svg class="tick" viewBox="0 0 10 10"><circle cx="5" cy="5" r="5" fill="#fff"/><path d="M2.6 5.2l1.6 1.6 3.2-3.4" stroke="#1ba9d6" stroke-width="1.4" fill="none"/></svg>Sod Lawn Services</li>
      <li><svg class="tick" viewBox="0 0 10 10"><circle cx="5" cy="5" r="5" fill="#fff"/><path d="M2.6 5.2l1.6 1.6 3.2-3.4" stroke="#1ba9d6" stroke-width="1.4" fill="none"/></svg>Lawn Care</li>
      <li><svg class="tick" viewBox="0 0 10 10"><circle cx="5" cy="5" r="5" fill="#fff"/><path d="M2.6 5.2l1.6 1.6 3.2-3.4" stroke="#1ba9d6" stroke-width="1.4" fill="none"/></svg>Sprinkler Systems</li>
      <li><svg class="tick" viewBox="0 0 10 10"><circle cx="5" cy="5" r="5" fill="#fff"/><path d="M2.6 5.2l1.6 1.6 3.2-3.4" stroke="#1ba9d6" stroke-width="1.4" fill="none"/></svg>Lawn Maintenance</li>
      <li><svg class="tick" viewBox="0 0 10 10"><circle cx="5" cy="5" r="5" fill="#fff"/><path d="M2.6 5.2l1.6 1.6 3.2-3.4" stroke="#1ba9d6" stroke-width="1.4" fill="none"/></svg>Stone Landscaping</li>
    </ul>
  </div>

  <div class="front__offer">
    <p class="offer-amount">$50.00 <small>OFF</small></p>
    <p class="offer-terms">with signing up for one of our routine<br>maintenance programs, or</p>
    <p class="offer-alt">1 FREE IRRIGATION INSPECTION</p>
    <div class="offer-rule"></div>
    <p class="offer-web">WWW.SHOREGARDENSFL.COM</p>
  </div>

  <div class="tile tile--dark tile--estimates"><strong>FREE</strong><span>ESTIMATES</span></div>
  <div class="photo photo--garden-bed" role="img" aria-label="Photo of a tropical flower bed with red bromeliads"></div>
  <div class="photo photo--paver-path" role="img" aria-label="Photo of a brick paver walkway lined with flowers"></div>
  <div class="photo photo--pool-deck" role="img" aria-label="Photo of a lawn with stepping stones beside a pool"></div>
  <div class="tile tile--dark tile--licensed"><span>FULLY</span><strong>LICENSED</strong><span>AND INSURED</span></div>

  <div class="front__call">
    <span class="call-label">CALL US NOW!</span>
    <span class="call-phone">
      <svg class="phone-icon" viewBox="0 0 20 20"><circle cx="10" cy="10" r="8.6" fill="none" stroke="#1ba9d6" stroke-width="1.8"/><path d="M7 5.5l1.6 2.4-1 1.1a6 6 0 0 0 3.4 3.4l1.1-1 2.4 1.6-.8 1.6c-3.8.4-8.1-3.9-7.7-7.7z" fill="#1ba9d6"/></svg>
      352-555-0148
    </span>
  </div>

  <svg class="swoosh" width="656" height="470" viewBox="0 0 656 470">
    <path d="M386 0 L386 240 Q384 380 352 470" fill="none" stroke="#fff" stroke-width="12"/>
    <path d="M382 0 L382 240 Q380 378 346 470" fill="none" stroke="#1ba9d6" stroke-width="7"/>
  </svg>

  <div class="guarantee-seal"></div>
</article>

<article class="postcard postcard--back">
  <div class="photo back__hero" role="img" aria-label="Photo of a lit resort pool with lounge chairs and tropical plants at dusk"></div>

  <svg class="back__panel-shape" width="656" height="470" viewBox="0 0 656 470">
    <defs>
      <radialGradient id="panelGlow" cx="0.45" cy="0.45" r="0.7">
        <stop offset="0" stop-color="#4a4f53"/>
        <stop offset="1" stop-color="#222629"/>
      </radialGradient>
    </defs>
    <path d="M330 200 Q500 150 656 132 L656 470 L330 470 Z" fill="#fff"/>
    <path d="M0 168 Q180 120 360 162 Q400 172 392 230 L380 380 Q374 440 352 470 L0 470 Z" fill="url(#panelGlow)"/>
    <path d="M0 168 Q180 120 360 162 Q400 172 392 230 L380 380 Q374 440 352 470" fill="none" stroke="#1ba9d6" stroke-width="6"/>
    <path d="M0 160 Q180 112 362 154" fill="none" stroke="#fff" stroke-width="3"/>
  </svg>

  <div class="back__content">
    <div class="brand-name">Shore Gardens</div>
    <p class="tagline">Enjoy your yard this summer</p>
    <ul class="features-list">
      <li><svg class="tick" viewBox="0 0 10 10"><circle cx="5" cy="5" r="5" fill="#fff"/><path d="M2.6 5.2l1.6 1.6 3.2-3.4" stroke="#2d3134" stroke-width="1.4" fill="none"/></svg>Hardscaping</li>
      <li><svg class="tick" viewBox="0 0 10 10"><circle cx="5" cy="5" r="5" fill="#fff"/><path d="M2.6 5.2l1.6 1.6 3.2-3.4" stroke="#2d3134" stroke-width="1.4" fill="none"/></svg>Lawn care and maintenance</li>
      <li><svg class="tick" viewBox="0 0 10 10"><circle cx="5" cy="5" r="5" fill="#fff"/><path d="M2.6 5.2l1.6 1.6 3.2-3.4" stroke="#2d3134" stroke-width="1.4" fill="none"/></svg>Stone landscaping</li>
      <li><svg class="tick" viewBox="0 0 10 10"><circle cx="5" cy="5" r="5" fill="#fff"/><path d="M2.6 5.2l1.6 1.6 3.2-3.4" stroke="#2d3134" stroke-width="1.4" fill="none"/></svg>Sod lawn work</li>
    </ul>
    <div class="back__rule"></div>
    <div class="back__call">
      <span class="call-label">CALL US NOW!</span>
      <span class="call-phone">
        <svg class="phone-icon" viewBox="0 0 20 20"><circle cx="10" cy="10" r="8.6" fill="none" stroke="#1ba9d6" stroke-width="1.8"/><path d="M7 5.5l1.6 2.4-1 1.1a6 6 0 0 0 3.4 3.4l1.1-1 2.4 1.6-.8 1.6c-3.8.4-8.1-3.9-7.7-7.7z" fill="#1ba9d6"/></svg>
        352-555-0148
      </span>
    </div>
    <p class="back__web">WWW.SHOREGARDENSFL.COM</p>
  </div>

  <div class="offer-bubble offer-bubble--discount"><span>$50.00 <small>OFF</small></span></div>
  <div class="offer-bubble offer-bubble--inspection"><span>OR</span><span>1 FREE IRRIGATION<br>INSPECTION</span></div>
</article>

</body>
</html>
```